Funeral Service App for our Client

Our client would like an app that celebrates and helps remember loved one's lives. We need an app design that provides soft tones and a peaceful feel. It should have a hero background that takes up most of the top part. It needs to provide three clickable options towards the bottom that are stacked vertically on the main page and the buttons need to seem like lables.

The first button would display another page and that page will have a collapsable search box at the top, and below it, a hero image of the deceased person. There should be a section below the image for traversing to next and previous images. Below this middle section, a text area that can hold scrollable text for an obiturary

The second button should bring up a new page (or view) that has an image list of upcoming services for that funeral home. Images should be on the left and descriptions on the right. Below each image and description should be 2 label buttons (or surprise us with a better UI) that can launch one of two pages. The left button launches the same view as the first button from the main page of the app. The right button will refresh the page with a contextual search of relatives who have also been deceased

The third button from the main page will behave like the second button but the listings will be that of affiliated funeral service providers. No label buttons below this image list but clicking the image will launch a webview page for that affiliate.

Please also include responsive designs for landscape modes

Target Market(s)

United States funeral directors

Industry/Entity Type

Professional Service

Font styles to use
Sans Serif

Colors
fac994
34a6d7
fff3d1
cee9f5

Requirements
Must have
• non platform specific design that can work equally on IOS, Android or Windows
Nice to have
• use own judgement on colors even though I provided a range

```html
<!DOCTYPE html>
<html lang="en">
<head>
<meta charset="utf-8">
<title>Ever Remembered – App Screens</title>
<link href="https://fonts.googleapis.com/css2?family=Heebo:wght@300;400;500&display=swap" rel="stylesheet">
<style>
:root{
  --stage:#151515;
  --gold:#b8860b;
  --gold-dark:#a57708;
  --peach:#e9a66a;
  --peach-light:#f6cfa3;
  --cream:#fff3d1;
  --white:#ffffff;
  --ink:#1e1e1e;
  --muted:#6d6d6d;
  --rule:#e4e4e4;
}
*{box-sizing:border-box;margin:0;padding:0}
html,body{width:1200px;height:1022px;overflow:hidden;background:var(--stage);font-family:"Heebo",Arial,sans-serif}
.canvas{position:relative;width:1200px;height:1022px}
.screen{position:absolute;top:168px;width:320px;height:568px;overflow:hidden}
.screen--home{left:46px}
.screen--services{left:440px;background:linear-gradient(180deg,#e8a56b 0%,#efc7a0 45%,#e8b07c 100%)}
.screen--profile{left:828px;background:linear-gradient(180deg,#e9a466 0%,#eab07a 50%,#d99a5c 100%)}
.status-bar{position:absolute;top:0;left:0;right:0;height:16px;display:flex;justify-content:space-between;align-items:center;padding:0 6px;font-size:10px;color:rgba(255,255,255,.9);z-index:3}
.status-bar .battery{display:inline-block;width:18px;height:7px;background:#fff;border-radius:1px;vertical-align:middle;margin-left:3px}
.hero-scene{position:absolute;inset:0;background:
  radial-gradient(ellipse 70% 18% at 50% 12%,rgba(255,246,235,.85),rgba(255,246,235,0) 70%),
  linear-gradient(180deg,#d9935a 0%,#f2c49a 20%,#f5a85c 42%,#e78a32 58%,#f0b270 78%,#f3c98e 100%)}
.app-name{position:absolute;top:50px;left:0;right:0;text-align:center;font-size:26px;font-weight:500;color:var(--gold);z-index:2}
.search-field{position:absolute;top:170px;left:13px;width:293px;height:47px;background:var(--white);border-radius:24px;display:flex;align-items:center;padding:0 12px 0 16px;font-size:14px;color:#c29a4a;justify-content:space-between;z-index:2;box-shadow:0 2px 6px rgba(0,0,0,.08)}
.icon-dot{width:21px;height:21px;border-radius:50%;background:var(--gold);display:flex;align-items:center;justify-content:center}
.nav-label{position:absolute;top:486px;width:68px;height:68px;border-radius:50%;background:var(--white);display:flex;align-items:center;justify-content:center;z-index:2;box-shadow:0 2px 8px rgba(0,0,0,.12)}
.screen-title{position:absolute;top:28px;left:0;right:0;text-align:center;color:var(--white);font-size:15px;font-weight:400;letter-spacing:.2px}
.round-btn{position:absolute;top:27px;width:21px;height:21px;border-radius:50%;background:rgba(255,255,255,.9);display:flex;align-items:center;justify-content:center}
.service-card{position:absolute;left:9px;width:301px;height:141px;background:var(--white);border-radius:6px;box-shadow:0 2px 6px rgba(0,0,0,.12)}
.avatar{position:absolute;left:12px;top:13px;width:69px;height:69px;border-radius:50%;background:linear-gradient(135deg,#c9d8df,#9fb4bf)}
.service-card .name{position:absolute;top:14px;left:90px;right:0;text-align:center;font-size:15px;font-weight:500;color:var(--ink)}
.dates{position:absolute;top:44px;width:100px;text-align:center;margin-left:-50px}
.dates .label{font-size:9px;color:var(--muted);display:block}
.dates .value{font-size:13px;color:var(--ink);display:block;margin-top:3px}
.card-rule{position:absolute;left:12px;right:12px;top:94px;border-top:1px solid var(--rule)}
.link-btn{position:absolute;top:111px;left:83px;width:80px;text-align:center;font-size:11px;font-weight:500;letter-spacing:.5px;color:var(--gold)}
.pill-btn{position:absolute;top:103px;left:179px;width:110px;height:30px;border-radius:15px;background:var(--gold);color:var(--white);font-size:11px;font-weight:500;letter-spacing:.5px;display:flex;align-items:center;justify-content:center}
.photo-stack{position:absolute;left:27px;top:69px;width:265px;height:20px;background:#7e97a8;border-radius:3px}
.portrait{position:absolute;left:13px;top:78px;width:293px;height:292px;border-radius:3px;background:linear-gradient(180deg,#c7d7da 0%,#b4cfd2 45%,#e9ecea 100%);box-shadow:0 3px 8px rgba(0,0,0,.25)}
.slide-arrow{position:absolute;top:342px;width:22px;height:22px;border-radius:50%;background:rgba(255,255,255,.9);display:flex;align-items:center;justify-content:center}
.life-dates{position:absolute;top:396px;left:0;right:0;display:flex;color:var(--white)}
.life-dates div{flex:1;text-align:center}
.life-dates .label{font-size:10px;display:block}
.life-dates .value{font-size:15px;display:block;margin-top:2px}
.life-dates .divider{flex:0 0 1px;background:rgba(255,255,255,.6);height:28px}
.obituary{position:absolute;top:458px;left:12px;right:12px;text-align:center;color:var(--white);font-size:14px;line-height:17.5px;font-weight:300}
.brand-name{position:absolute;top:880px;left:0;right:0;text-align:center;font-size:56px;font-weight:500;color:var(--gold)}
</style>
</head>
<body>
<div class="canvas">

  <section class="screen screen--home">
    <div class="hero-scene" role="img" aria-label="Soft cloudy sky above a misty golden forest at sunrise"></div>
    <div class="status-bar"><span>●●●●● Velora</span><span>7:28 AM</span><span>100%<i class="battery"></i></span></div>
    <div class="app-name">Ever Remembered</div>
    <div class="search-field"><span>enter a hero’s name</span>
      <span class="icon-dot"><svg width="11" height="11" viewBox="0 0 12 12"><circle cx="5" cy="5" r="3.5" fill="none" stroke="#fff" stroke-width="1.6"/><line x1="7.6" y1="7.6" x2="11" y2="11" stroke="#fff" stroke-width="1.8"/></svg></span></div>
    <div class="nav-label" style="left:13px"><svg width="28" height="28" viewBox="0 0 28 28" fill="none" stroke="#b8860b" stroke-width="1.6"><rect x="3" y="5" width="22" height="20" rx="2"/><line x1="3" y1="10" x2="25" y2="10"/><line x1="9" y1="2" x2="9" y2="7"/><line x1="19" y1="2" x2="19" y2="7"/><g fill="#b8860b" stroke="none"><rect x="7" y="13" width="3" height="3"/><rect x="12.5" y="13" width="3" height="3"/><rect x="18" y="13" width="3" height="3"/><rect x="7" y="18" width="3" height="3"/><rect x="12.5" y="18" width="3" height="3"/><rect x="18" y="18" width="3" height="3"/></g></svg></div>
    <div class="nav-label" style="left:125px"><svg width="30" height="26" viewBox="0 0 30 26" fill="none" stroke="#b8860b" stroke-width="1.6"><rect x="2" y="3" width="26" height="20" rx="2"/><circle cx="15" cy="11" r="4" fill="#b8860b"/><path d="M8 22c1-4 4-6 7-6s6 2 7 6" fill="#b8860b"/></svg></div>
    <div class="nav-label" style="left:237px"><svg width="30" height="26" viewBox="0 0 30 26" fill="none" stroke="#b8860b" stroke-width="1.6"><path d="M15 5C11 3 6 3 3 4v18c3-1 8-1 12 1 4-2 9-2 12-1V4c-3-1-8-1-12 1z"/><line x1="15" y1="5" x2="15" y2="23"/><line x1="6" y1="9" x2="12" y2="9"/><line x1="6" y1="13" x2="12" y2="13"/><line x1="6" y1="17" x2="12" y2="17"/><line x1="18" y1="9" x2="24" y2="9"/><line x1="18" y1="13" x2="24" y2="13"/><line x1="18" y1="17" x2="24" y2="17"/></svg></div>
  </section>

  <section class="screen screen--services">
    <div class="status-bar"><span>●●●●● Velora</span><span>7:28 AM</span><span>100%<i class="battery"></i></span></div>
    <div class="round-btn" style="left:9px"><svg width="11" height="11" viewBox="0 0 12 12"><path d="M5 2L1.5 5.5 5 9M2 5.5h5a3 3 0 0 1 3 3v1" fill="none" stroke="#d99a5c" stroke-width="1.6"/></svg></div>
    <h1 class="screen-title">UPCOMING SERVICES</h1>

    <article class="service-card" style="top:60px">
      <div class="avatar" role="img" aria-label="Portrait photo of Daniel Hartwell"></div>
      <div class="name">DANIEL HARTWELL</div>
      <div class="dates" style="left:128px"><span class="label">BORN</span><span class="value">12 SEP 1973</span></div>
      <div class="dates" style="left:251px"><span class="label">DIED</span><span class="value">30 NOV 2013</span></div>
      <div class="card-rule"></div>
      <div class="link-btn">BUTTON ONE</div><div class="pill-btn">MORE INFO</div>
    </article>
    <article class="service-card" style="top:210px">
      <div class="avatar" role="img" aria-label="Portrait photo of Margaret Lane" style="background:linear-gradient(135deg,#e6d2b0,#b89a7a)"></div>
      <div class="name">MARGARET LANE</div>
      <div class="dates" style="left:128px"><span class="label">BORN</span><span class="value">1 APR 1992</span></div>
      <div class="dates" style="left:251px"><span class="label">DIED</span><span class="value">28 DEC 2016</span></div>
      <div class="card-rule"></div>
      <div class="link-btn">BUTTON ONE</div><div class="pill-btn">MORE INFO</div>
    </article>
    <article class="service-card" style="top:360px">
      <div class="avatar" role="img" aria-label="Portrait photo of Eleanor Brooks" style="background:linear-gradient(135deg,#d46a4e,#6a3b2e)"></div>
      <div class="name">ELEANOR BROOKS</div>
      <div class="dates" style="left:128px"><span class="label">BORN</span><span class="value">21 OCT 1956</span></div>
      <div class="dates" style="left:251px"><span class="label">DIED</span><span class="value">27 DEC 2016</span></div>
      <div class="card-rule"></div>
      <div class="link-btn">BUTTON ONE</div><div class="pill-btn">MORE INFO</div>
    </article>
    <article class="service-card" style="top:510px">
      <div class="avatar" role="img" aria-label="Portrait photo of Thomas Avery" style="background:linear-gradient(135deg,#6b4a3a,#1f1a18)"></div>
      <div class="name">THOMAS AVERY</div>
      <div class="dates" style="left:128px"><span class="label">BORN</span></div>
      <div class="dates" style="left:251px"><span class="label">DIED</span></div>
    </article>
  </section>

  <section class="screen screen--profile">
    <div class="status-bar"><span>●●●●● Velora</span><span>7:28 AM</span><span>100%<i class="battery"></i></span></div>
    <div class="round-btn" style="left:9px"><svg width="11" height="11" viewBox="0 0 12 12"><path d="M5 2L1.5 5.5 5 9M2 5.5h5a3 3 0 0 1 3 3v1" fill="none" stroke="#d99a5c" stroke-width="1.6"/></svg></div>
    <h1 class="screen-title">DANIEL HARTWELL</h1>
    <div class="round-btn" style="right:9px"><svg width="11" height="11" viewBox="0 0 12 12"><circle cx="5" cy="5" r="3.5" fill="none" stroke="#d99a5c" stroke-width="1.5"/><line x1="7.6" y1="7.6" x2="11" y2="11" stroke="#d99a5c" stroke-width="1.6"/></svg></div>
    <div class="photo-stack"></div>
    <div class="portrait" role="img" aria-label="Portrait photo of Daniel Hartwell by the sea"></div>
    <div class="slide-arrow" style="left:21px"><svg width="10" height="10" viewBox="0 0 10 10"><path d="M6.5 1.5L3 5l3.5 3.5" fill="none" stroke="#555" stroke-width="1.6"/></svg></div>
    <div class="slide-arrow" style="left:276px"><svg width="10" height="10" viewBox="0 0 10 10"><path d="M3.5 1.5L7 5 3.5 8.5" fill="none" stroke="#555" stroke-width="1.6"/></svg></div>
    <div class="life-dates">
      <div><span class="label">BORN</span><span class="value">12 SEP 1973</span></div>
      <span class="divider"></span>
      <div><span class="label">DIED</span><span class="value">30 NOV 2013</span></div>
    </div>
    <p class="obituary">Lorem ipsum dolor sit amet, consectetur adipiscing elit. Vestibulum dolor elit, mattis non quam sed, sodales vestibulum justo. Cras sed accumsan mi, in auctor nisi.</p>
  </section>

  <div class="brand-name">Ever Remembered</div>
</div>
</body>
</html>
```